Business Card Design

I need a Business Card that will catch the attention that will not get thrown in a Drawer. I have 23 companies I use for Auto, Home, Life, and Business Insurance. I make sure that people have the best coverage for the $ spent.

Industry/Entity Type

Business

Contact Information for Business Card

Torvin Insurance Agency, Inc., Derek Halloway, 4735 West Fallow Lane Larkford, Westmora 52913 555-287-6194, www.torvinagency-example.com, Friendlink, ProNet, CircleUp

```html
<!DOCTYPE html>
<html lang="en">
<head>
<meta charset="utf-8">
<title>Torvin Insurance Agency – Business Card</title>
<link rel="stylesheet" href="https://fonts.googleapis.com/css2?family=Bodoni+Moda:wght@400;700&family=Jost:wght@400&display=swap">
<style>
  :root {
    --charcoal: #1f2321;
    --sage-text: #a9c98c;
    --rule-green: #b8dc8e;
    --olive-edge: #565b22;
    --olive-mid: #8a9a45;
    --glow-green: #c6f59c;
    --logo-white: #ffffff;
    --tagline-grey: #b9c3c3;
    --ink-dark: #2f3331;
    --phone-red: #780a0b;
  }
  * { margin: 0; padding: 0; box-sizing: border-box; }
  html, body {
    width: 1200px;
    height: 702px;
    overflow: hidden;
    background: #ffffff;
  }
  .card {
    position: relative;
    width: 1200px;
    height: 702px;
    overflow: hidden;
    background: var(--charcoal);
  }
  .card__top {
    position: absolute;
    left: 0; top: 0;
    width: 1200px;
    height: 459px;
    background: var(--charcoal);
  }
  .links {
    position: absolute;
    top: 46px;
    width: 100%;
    text-align: center;
    font-family: "Bodoni Moda", "Didot", serif;
    font-size: 37px;
    letter-spacing: 1px;
    color: var(--sage-text);
  }
  .links__sep { padding: 0 6px; }
  .brand {
    position: absolute;
    top: 176px;
    width: 100%;
    text-align: center;
    font-family: "Bodoni Moda", "Didot", serif;
    font-weight: 400;
    font-size: 170px;
    line-height: 1;
    color: var(--logo-white);
  }
  .tagline {
    position: absolute;
    top: 370px;
    width: 100%;
    text-align: center;
    font-family: "Bodoni Moda", "Didot", serif;
    font-size: 54px;
    letter-spacing: -1.5px;
    color: var(--tagline-grey);
  }
  .divider {
    position: absolute;
    left: 0; top: 459px;
    width: 1200px;
    height: 3px;
    background: var(--rule-green);
  }
  .card__bottom {
    position: absolute;
    left: 0; top: 462px;
    width: 1200px;
    height: 240px;
    background:
      radial-gradient(ellipse 520px 260px at 50% 100%, var(--glow-green) 0%, var(--olive-mid) 55%, var(--olive-edge) 100%);
  }
  .contact {
    position: absolute;
    top: 10px;
    width: 100%;
    text-align: center;
    font-family: "Jost", "Futura", sans-serif;
    font-size: 45px;
    line-height: 50px;
    color: var(--ink-dark);
  }
  .phone {
    position: absolute;
    top: 134px;
    width: 100%;
    text-align: center;
    font-family: "Bodoni Moda", "Times New Roman", serif;
    font-weight: 700;
    font-size: 46px;
    color: var(--phone-red);
  }
</style>
</head>
<body>
  <div class="card">
    <header class="card__top">
      <p class="links">www.torvinagency-example.com<span class="links__sep">|</span>Friendlink<span class="links__sep">|</span>ProNet<span class="links__sep">|</span>CircleUp</p>
      <h1 class="brand">Torvin</h1>
      <p class="tagline">Insurance Agency, Inc.</p>
    </header>
    <div class="divider"></div>
    <section class="card__bottom">
      <p class="contact">Derek Halloway, 4735 West Fallow Lane<br>Larkford, Westmora 52913</p>
      <p class="phone">555-287-6194</p>
    </section>
  </div>
</body>
</html>
```